Disruptive Wine Company Business Card

We need a SINGLE-SIDED business card for a wine company that is going to destroy the wine industry as you know it.

The business is meant to be fun, easy, approachable & high tech.

Although the logo is purple & yellow we do not want purple/yellow (bright colored) cards. Maybe a light grey background with the logo on it. Purple or yellow lines/curves in the card design is OK, but it should not be too bright.

These cards will be given out to customers who want to retain the store information or pass the cards along to their friends.

Target Market(s)

young, hip, city dwelling wine lovers

Looking for a simple but unique design that isn't showy, but will be eye grabbing.

Requirements
Must have
• An eye catching design
Should not have
• Should not be too "showy".

```html
<!DOCTYPE html>
<html lang="en">
<head>
<meta charset="utf-8">
<title>Vinlo Wine Company – Business Card</title>
<link rel="stylesheet" href="https://fonts.googleapis.com/css2?family=Lato:wght@400;700&display=swap">
<style>
  :root {
    --page-bg: #e9e7e4;
    --card-top: #a3a7ad;
    --card-mid: #cfd1d4;
    --card-bottom: #e6e7e8;
    --plum: #8d3f84;
    --gold: #e0ab4a;
    --gold-light: #f1c873;
    --ink: #363636;
    --ink-soft: #474747;
  }
  * { margin: 0; padding: 0; box-sizing: border-box; }
  html, body {
    width: 1200px; height: 970px; overflow: hidden;
    background: var(--page-bg);
    font-family: "Lato", Arial, sans-serif;
  }
  .card {
    position: absolute; left: 100px; top: 207px;
    width: 1000px; height: 555px;
    background: linear-gradient(180deg, var(--card-top) 0%, var(--card-mid) 45%, var(--card-bottom) 100%);
    border: 1px solid #b9bbbe;
    box-shadow: 0 10px 30px rgba(0,0,0,.15);
    overflow: hidden;
  }
  .card__swoosh { position: absolute; inset: 0; }
  .holder { position: absolute; left: 72px; top: 50px; }
  .holder__name { color: var(--plum); font-weight: 700; font-size: 35px; line-height: 1.1; }
  .holder__role { color: var(--ink-soft); font-size: 28px; margin-top: 6px; }
  .contact { position: absolute; left: 72px; top: 254px; list-style: none; }
  .contact__item {
    display: flex; align-items: center; gap: 16px;
    height: 39px; font-size: 28px; color: var(--ink);
  }
  .contact__icon { width: 28px; height: 28px; flex: none; fill: var(--plum); }
  .contact__item--address { align-items: flex-start; height: auto; margin-top: 28px; line-height: 38px; gap: 12px; }
  .contact__item--address .contact__icon { margin-top: 5px; width: 24px; }
  .brand {
    position: absolute; left: 752px; top: 38px; width: 220px;
    display: flex; flex-direction: column; align-items: center;
  }
  .brand__mark { width: 120px; height: 120px; border-radius: 50%; background: var(--plum); opacity: .85; }
  .brand__name {
    margin-top: 30px; color: var(--gold); font-weight: 400;
    font-size: 44px; letter-spacing: 8px; line-height: 1;
  }
  .brand__tagline {
    margin-top: 6px; color: var(--gold); font-weight: 400;
    font-size: 12px; letter-spacing: 3px;
  }
  .social { position: absolute; left: 830px; top: 486px; display: flex; gap: 16px; }
  .social__link { width: 28px; height: 28px; background: var(--plum); border-radius: 3px; }
</style>
</head>
<body>
  <article class="card">
    <svg class="card__swoosh" width="1000" height="555" viewBox="0 0 1000 555" aria-hidden="true">
      <defs>
        <linearGradient id="goldBand" x1="0" x2="1">
          <stop offset="0" stop-color="var(--gold)"/>
          <stop offset=".5" stop-color="var(--gold-light)"/>
          <stop offset="1" stop-color="var(--gold)"/>
        </linearGradient>
      </defs>
      <path d="M0 165 C260 140 520 175 1000 365" fill="none" stroke="#f4f4f4" stroke-width="3" opacity=".8"/>
      <path d="M0 172 C260 150 560 190 1000 374 L1000 382 C580 230 300 215 0 225 Z" fill="url(#goldBand)"/>
      <path d="M0 232 C300 222 580 238 1000 390" fill="none" stroke="#f4f4f4" stroke-width="2" opacity=".7"/>
    </svg>

    <header class="holder">
      <h1 class="holder__name">Mara Lindqvist</h1>
      <p class="holder__role">Director</p>
    </header>

    <ul class="contact">
      <li class="contact__item">
        <svg class="contact__icon" viewBox="0 0 24 24"><path d="M3 8c0-3 4-4 9-4s9 1 9 4v2h-5V8H8v2H3z"/><path d="M6 11h12l2 8H4z"/><circle cx="12" cy="15" r="2.2" fill="#ddd"/></svg>
        <span>010 234 5678</span>
      </li>
      <li class="contact__item">
        <svg class="contact__icon" viewBox="0 0 24 24"><path d="M7 2h10a1.5 1.5 0 0 1 1.5 1.5v17A1.5 1.5 0 0 1 17 22H7a1.5 1.5 0 0 1-1.5-1.5v-17A1.5 1.5 0 0 1 7 2zm1 3v12h8V5z"/><circle cx="12" cy="19.5" r="1" fill="#ddd"/></svg>
        <span>020 345 6789</span>
      </li>
      <li class="contact__item">
        <svg class="contact__icon" viewBox="0 0 24 24"><path d="M2 5h20v14H2z"/><path d="M2 5l10 8 10-8" fill="none" stroke="#ddd" stroke-width="1.6"/></svg>
        <span>hello@vinlowine.com</span>
      </li>
      <li class="contact__item">
        <svg class="contact__icon" viewBox="0 0 24 24"><circle cx="12" cy="12" r="10"/><g fill="none" stroke="#ddd" stroke-width="1.3"><ellipse cx="12" cy="12" rx="4.5" ry="10"/><path d="M2 12h20M4 7h16M4 17h16"/></g></svg>
        <span>www.vinlowine.com</span>
      </li>
      <li class="contact__item contact__item--address">
        <svg class="contact__icon" viewBox="0 0 24 24"><path d="M12 1a8 8 0 0 1 8 8c0 6-8 14-8 14S4 15 4 9a8 8 0 0 1 8-8z"/><circle cx="12" cy="9" r="3" fill="#ddd"/></svg>
        <address style="font-style:normal">74 Harlow St, Brookfield,<br>NY 10123, USA</address>
      </li>
    </ul>

    <div class="brand">
      <span class="brand__mark" aria-hidden="true"></span>
      <span class="brand__name">VINLO</span>
      <span class="brand__tagline">WINE COMPANY</span>
    </div>

    <nav class="social" aria-label="Social profiles">
      <span class="social__link"></span>
      <span class="social__link"></span>
      <span class="social__link"></span>
    </nav>
  </article>
</body>
</html>
```